Stationery Design Project

I have recently had developed a logo for my new company Northwind Venture Partners -see logo attached.
I now need the following
1. Letterhead design as Word template
text needs to show the logo and then
Northwind Venture Partners Pty Ltd
ABN 83 402 615 294
Level 5, Harrow Building
17 Wexley Court
Baulkham Hills, NSW 2153
Tel: + 61(0)2 7314 2086
www.northwindventurepartners.example
dericp@northwindventurepartners.example
2. Business card -print ready -
Front side needs to show logo then text as follows
Deric Pellham
CEO
Level 5, Harrow Building
17 Wexley Court
Baulkham Hills, NSW 2153
T: + 61 (0)2 7314 2086
M: + 61 (0)438 772 104
dericp@brolvenco.example
On the back of the business card should appear the logo then text as follows
Correct text for the back of the card now in the attached word file please use bold and italics as indicated. Thanks
3. With compliments slip: Including logo + the web address www.northwindventurepartners.example
With compliments slip should fit 3 to an A4 sheet
4. Envelop design including logo + address
For the ethos of the company original brief for the logo below:
I am creating a new business advisory company called Northwind Venture Partners. the Web address will be www.northwindventurepartners.example This business is focused on assisting medium size businesses to achieve their growth objectives. The three pillars are self explanatory -it is focused on businesses that seek to build a global footprint, they seek to define/refine their business model and strategy, they are forward looking and focused on achieving growth.
The ethos of this company will be innovative thinking, passionate, dynamic, entrepreneurial this should reflected in the logo. That said the Logo should not be 'complicated' it should be simple and elegant...
Thanks Deric Pellham
Reason: I have been travelling all this week -so will only get a chance to review this weekend. Thanks
Target Market(s)
Medium sized business owners with sales between US$5m and $50m.
Industry/Entity Type
Business
Look and feel

```html
<!DOCTYPE html>
<html lang="en">
<head>
<meta charset="utf-8">
<title>Northwind Venture Partners – Business Card</title>
<link rel="stylesheet" href="https://fonts.googleapis.com/css2?family=Source+Sans+3:ital,wght@0,400;0,600;1,700&display=swap">
<style>
  :root {
    --stage: #ececec;
    --card-white: #ffffff;
    --brand-blue: #1a5fb4;
    --brand-blue-deep: #0d4fa8;
    --teal: #4aa9a4;
    --teal-light: #a9d8d6;
    --teal-pale: #cfe9e8;
    --ink: #3a3a3a;
    --ink-soft: #555;
  }
  * { box-sizing: border-box; margin: 0; padding: 0; }
  html, body { width: 1200px; height: 682px; overflow: hidden; }
  body {
    background: var(--stage);
    font-family: "Source Sans 3", "Myriad Pro", sans-serif;
    position: relative;
  }
  .card {
    position: absolute;
    top: 181px;
    width: 540px;
    height: 320px;
    border-radius: 22px;
    overflow: hidden;
    box-shadow: 0 8px 22px rgba(0,0,0,0.18);
  }
  .card--front { left: 40px; background: var(--card-white); }
  .card--back {
    left: 620px;
    background: linear-gradient(180deg, var(--teal-pale) 0%, var(--teal-light) 35%, var(--teal) 100%);
  }
  .wordmark {
    position: absolute;
    font-weight: 600;
    font-size: 34px;
    color: var(--brand-blue);
    display: flex;
    align-items: center;
    gap: 12px;
    white-space: nowrap;
  }
  .wordmark__square {
    width: 22px; height: 22px;
    background: var(--teal);
    display: inline-block;
  }
  .card--front .wordmark { left: 36px; top: 22px; }
  .card--back .wordmark { left: 36px; top: 38px; color: var(--brand-blue-deep); }

  .person {
    position: absolute; left: 0; right: 0; top: 84px;
    text-align: center;
    font-size: 20px; font-weight: 600; color: var(--brand-blue);
  }
  .person__role { font-weight: 400; font-size: 15px; color: var(--ink-soft); }

  .contacts {
    position: absolute; left: 0; right: 0; top: 120px;
    display: flex; justify-content: center; gap: 18px;
    font-size: 14px; color: var(--ink);
  }
  .contacts__col { display: flex; flex-direction: column; gap: 4px; justify-content: flex-end; }
  .contacts__col--left { text-align: right; padding-top: 14px; }
  .contacts__divider { width: 1px; background: #999; }
  .contact-line { display: flex; align-items: center; gap: 6px; }
  .contacts__col--left .contact-line { justify-content: flex-end; }
  .contact-line svg { width: 11px; height: 11px; fill: var(--ink-soft); flex: none; }

  .address {
    position: absolute; left: 0; right: 0; top: 178px;
    text-align: center; font-size: 12.5px; line-height: 1.35; color: var(--ink);
  }
  .wave { position: absolute; left: 0; top: 0; width: 540px; height: 320px; }
  .web {
    position: absolute; right: 30px; bottom: 16px;
    color: #fff; font-size: 15px;
  }

  .pitch {
    position: absolute; left: 40px; top: 120px; right: 30px;
    color: #fff;
  }
  .pitch__title { font-weight: 700; font-style: italic; font-size: 19px; margin-bottom: 6px; }
  .pitch__list { list-style: none; font-size: 15.5px; line-height: 1.3; }
  .pitch__list li { position: relative; padding-left: 14px; }
  .pitch__list li::before {
    content: ""; position: absolute; left: 0; top: 7px;
    width: 7px; height: 7px; border-radius: 50%; background: #fff;
  }
</style>
</head>
<body>
  <section class="card card--front" aria-label="Business card front">
    <svg class="wave" viewBox="0 0 540 320" aria-hidden="true">
      <defs>
        <linearGradient id="band" x1="0" x2="1" y1="0" y2="0">
          <stop offset="0" stop-color="#5fb7e4"/>
          <stop offset="1" stop-color="#0d4fa8"/>
        </linearGradient>
      </defs>
      <path d="M0 270 C160 288 320 238 540 234 L540 243 C330 248 170 298 0 283 Z" fill="#7cc3c0"/>
      <path d="M0 292 C170 306 340 254 540 250 L540 320 L0 320 Z" fill="url(#band)"/>
    </svg>

    <div class="wordmark"><span class="wordmark__square"></span>Northwind Venture Partners</div>

    <p class="person">Deric Pellham, <span class="person__role">CEO</span></p>

    <div class="contacts">
      <div class="contacts__col contacts__col--left">
        <span class="contact-line"><svg viewBox="0 0 10 10"><rect x="2.5" y="0" width="5" height="10" rx="1"/></svg>+ 61 438 772 104</span>
        <span class="contact-line"><svg viewBox="0 0 10 10"><path d="M2 0 L4 2.5 L3 4 C4 6 4.5 6.5 6 7 L7.5 6 L10 8 L8.5 10 C4 9.5 0.5 6 0 1.5 Z"/></svg>+ 61 (0)2 7314 2086</span>
      </div>
      <span class="contacts__divider"></span>
      <div class="contacts__col">
        <span class="contact-line"><svg viewBox="0 0 10 10"><rect x="0" y="4" width="10" height="6" rx="1"/><rect x="2" y="0" width="6" height="4"/></svg>+ 61 (0)2 5209 3371</span>
        <span class="contact-line"><svg viewBox="0 0 10 10"><path d="M0 2 H10 V9 H0 Z M0 2 L5 6 L10 2" /></svg>dericp@brolvenco.example</span>
      </div>
    </div>

    <p class="address">
      Northwind Venture Partners Pty Ltd<br>
      Level 8, Harrow Building<br>
      17 Wexley Court, Dunmore Vale, NSW 2871
    </p>

    <p class="web">www.northwindventurepartners.example</p>
  </section>

  <section class="card card--back" aria-label="Business card back">
    <div class="wordmark"><span class="wordmark__square"></span>Northwind Venture Partners</div>
    <div class="pitch">
      <p class="pitch__title">Develop the Right Strategy for your business</p>
      <ul class="pitch__list">
        <li>Be accountable - create your Advisory Board</li>
        <li>Build a Business Plan your team will implement</li>
        <li>Take your business global - Export Market Development</li>
        <li>CEO groups</li>
        <li>Presentations, Seminars, Conferences</li>
      </ul>
    </div>
  </section>
</body>
</html>
```